RLT PowerPoint

I am looking for a clean, corporate PowerPoint template.

I would like the following:
- title slide
- break slide
- blank slide with title (for graphs or graphics)
- an ending slide.

Target Market(s)

Business professionals, medium to large business clients.

Requirements
Must have
• Must incorporate the RLT logo in either the header or footer

```html
<!DOCTYPE html>
<html lang="en">
<head>
<meta charset="utf-8">
<title>RLT – Project Title</title>
<link rel="stylesheet" href="https://fonts.googleapis.com/css2?family=Gelasio:wght@400;700&family=Open+Sans:wght@400;700&family=Carlito&display=swap">
<style>
  :root {
    --header-dark: #2a54ad;
    --header-mid: #3f6fd6;
    --header-light: #4e87ef;
    --rule: #111111;
    --accent: #2f62c8;
    --navy: #2c55a8;
    --bar-mid: #4070cc;
    --bar-light: #5088ee;
    --bar-bright: #4078e0;
    --bar-grey: #808080;
    --ink: #1a1a1a;
    --footer-bg: #f2f2f2;
    --white: #ffffff;
  }
  * { margin: 0; padding: 0; box-sizing: border-box; }
  html, body { width: 1200px; height: 900px; overflow: hidden; background: var(--white); }
  .slide { position: relative; width: 1200px; height: 900px; overflow: hidden; background: var(--white); }

  .slide-header {
    position: absolute; left: 0; top: 0; width: 1200px; height: 93px;
    background: linear-gradient(90deg, var(--header-dark) 0%, var(--header-mid) 40%, var(--header-light) 78%, var(--header-dark) 100%);
    border-bottom: 4px solid var(--rule);
  }
  .slide-title {
    position: absolute; left: 30px; top: 18px;
    font-family: "Gelasio", Georgia, serif; font-weight: 700; font-size: 45px;
    color: var(--white); line-height: 1.1;
  }
  .header-mark {
    position: absolute; right: 10px; top: 8px;
    font-family: "Gelasio", Georgia, serif; font-weight: 400; font-size: 62px;
    color: rgba(255,255,255,0.18); line-height: 1;
  }

  .chart { position: absolute; left: 0; top: 0; width: 1200px; height: 900px; }
  .axis-label {
    position: absolute; font-family: "Open Sans", Tahoma, sans-serif; font-size: 19px;
    color: var(--ink); white-space: nowrap; line-height: 1;
  }
  .axis-label.y { right: 910px; transform: translateY(-50%); }
  .axis-label.x { top: 701px; transform: translateX(-50%); }

  .slide-footer {
    position: absolute; left: 0; top: 809px; width: 1200px; height: 91px;
    background: var(--footer-bg); border-top: 4px solid var(--accent);
  }
  .brand {
    position: absolute; left: 22px; top: 22px;
    font-family: "Gelasio", Georgia, serif; font-weight: 400; font-size: 34px;
    color: var(--navy); white-space: nowrap; line-height: 1;
  }
  .copyright {
    position: absolute; left: 894px; top: 36px;
    font-family: "Carlito", Calibri, sans-serif; font-size: 22px; color: var(--ink); line-height: 1;
  }
  .page-number {
    position: absolute; left: 1099px; top: 20px; width: 54px; height: 54px; border-radius: 50%;
    background: var(--accent); color: var(--white);
    font-family: "Open Sans", Arial, sans-serif; font-weight: 700; font-size: 21px;
    display: flex; align-items: center; justify-content: center;
  }
</style>
</head>
<body>
<div class="slide">
  <header class="slide-header">
    <h1 class="slide-title">Project Title here</h1>
    <span class="header-mark">RLT</span>
  </header>

  <svg class="chart" viewBox="0 0 1200 900" width="1200" height="900" aria-label="Bar chart">
    <line x1="306.5" y1="192" x2="306.5" y2="676" stroke="var(--rule)" stroke-width="2"/>
    <line x1="306" y1="675.5" x2="1137" y2="675.5" stroke="var(--rule)" stroke-width="2"/>
    <rect x="306" y="518" width="54" height="157" fill="var(--bar-mid)"/>
    <rect x="372" y="393" width="69" height="282" fill="var(--bar-light)"/>
    <rect x="457" y="443" width="68" height="232" fill="var(--bar-light)"/>
    <rect x="537" y="536" width="68" height="139" fill="var(--navy)"/>
    <rect x="624" y="633" width="72" height="42" fill="var(--bar-bright)"/>
    <rect x="710" y="660" width="82" height="15" fill="var(--bar-grey)"/>
    <rect x="802" y="234" width="67" height="441" fill="var(--navy)"/>
    <rect x="885" y="630" width="71" height="45" fill="var(--bar-light)"/>
    <rect x="969" y="653" width="71" height="22" fill="var(--bar-bright)"/>
    <rect x="1056" y="660" width="81" height="15" fill="var(--bar-grey)"/>
  </svg>

  <span class="axis-label y" style="top:219px">Lorem ipsum text here</span>
  <span class="axis-label y" style="top:296px">Lorem ipsum text here</span>
  <span class="axis-label y" style="top:396px">Lorem ipsum text here</span>
  <span class="axis-label y" style="top:522px">Lorem ipsum text here</span>
  <span class="axis-label y" style="top:668px">Lorem ipsum text here</span>

  <span class="axis-label x" style="left:406px">Lorem ipsum text here</span>
  <span class="axis-label x" style="left:692px">Lorem ipsum text here</span>
  <span class="axis-label x" style="left:1038px">Lorem ipsum text here</span>

  <footer class="slide-footer">
    <span class="brand">RLT Reed Lane Trust</span>
    <span class="copyright">Copyright text here</span>
    <span class="page-number">01</span>
  </footer>
</div>
</body>
</html>
```